Pinecrest Insurance Services - Application Designs

My company name is Pinecrest Insurance Services. We are a full service insurance brokerage.

I need an ACH Form (which is attached) to be created with my logo (which is also attached). Please make the ACH Form fillable for info to be entered manually.

In addition I need the Example Quote created with the same color scheme as the Pinecrest Logo. Please create the Example quote as a word document so I can edit the quote and save as a PDF. You can also send me different quote ideas as long as they have the same information on the quote I have attached.

For the Example Supplemental you can leave everything as is and just change the Pinecrest Logo to the attached Pinecrest Insurance Services Logo.

- Change all color-ways to the Pinecrest Insurance Services color-way logo
- Change all the Pinecrest logos to the Pinecrest logo
- Phone number to the company is (555) 317-2096
- Change anything that says Pinecrest to Pinecrest
- Company address is: 7810 Dunmore Ave, Unit B Studio City CA 91604
- Company Email address is Rory@Pinecrestinsurancegroup.example

Target Market(s)

Clients or Potential Clients

Industry/Entity Type

Insurance

Font styles to use
Serif

Colors
0054AA
0677BA
7BADD7
CADEEF
E8F1F8
00AB8E
00BBA5
67D7C9
C6EFE9
E9F9F6

Requirements
Must have
• Pinecrest Insurance Services Logo

```html
<!DOCTYPE html>
<html lang="en">
<head>
<meta charset="UTF-8">
<title>Pinecrest Insurance Services – Payment Authorization Form</title>
<link href="https://fonts.googleapis.com/css2?family=Source+Serif+4:opsz,wght@8..60,400;8..60,600;8..60,700&display=swap" rel="stylesheet">
<style>
  :root {
    --brand-blue: #0054AA;
    --brand-blue-mid: #0677BA;
    --brand-blue-soft: #7BADD7;
    --brand-teal: #00AB8E;
    --panel: #E8F1F8;
    --cell-line: #CADEEF;
    --label: #4f5a66;
    --muted: #6f7a86;
    --header-soft: #7BADD7;
    --white: #ffffff;
  }
  * { box-sizing: border-box; margin: 0; padding: 0; }
  html, body { width: 896px; height: 1200px; overflow: hidden; }
  body { background: var(--white); font-family: 'Source Serif 4', Georgia, serif; color: var(--label); position: relative; }
  .page-panel { position: absolute; left: 21px; top: 26px; width: 855px; height: 1105px; background: var(--panel); }
  .abs { position: absolute; }

  .brand { left: 63px; top: 78px; width: 310px; text-align: center; color: var(--brand-blue); font-weight: 700; }
  .brand-name { font-size: 42px; letter-spacing: 0.5px; line-height: 48px; }
  .brand-sub { font-size: 14px; letter-spacing: 5px; line-height: 22px; margin-top: 4px; }

  .auth-title { left: 409px; top: 45px; width: 448px; height: 24px; background: var(--header-soft); color: var(--white); font-weight: 700; font-size: 13px; line-height: 24px; padding-left: 11px; }
  .auth-table { left: 414px; top: 75px; width: 438px; border-collapse: collapse; }
  .auth-table td { height: 32px; border: 1px solid var(--cell-line); font-size: 13px; letter-spacing: 0.4px; padding-left: 7px; }
  .auth-table td.label { width: 150px; }

  .band { left: 56px; width: 801px; height: 27px; background: linear-gradient(90deg, var(--brand-blue), var(--brand-blue-mid)); color: var(--white); font-size: 13.5px; line-height: 27px; padding: 0 14px 0 17px; display: flex; align-items: center; }
  .band-title { font-weight: 700; }
  .band-note { font-size: 9px; font-weight: 600; margin-left: 12px; }
  .band-option { margin-left: auto; letter-spacing: 0.3px; display: flex; align-items: center; gap: 14px; }
  .option-box { width: 18px; height: 18px; background: var(--white); display: inline-block; }

  .field-table { left: 63px; width: 789px; border-collapse: collapse; }
  .field-table td { height: 32px; border: 1px solid var(--cell-line); font-size: 13.5px; padding-left: 3px; position: relative; }
  .field-table td.label { width: 170px; }
  .hint { position: absolute; right: 8px; top: 7px; font-size: 7.5px; color: var(--label); }

  .pay-table { border-collapse: collapse; }
  .pay-table td { height: 31px; border: 1.5px solid var(--brand-teal); font-size: 13.5px; font-weight: 700; padding-left: 5px; white-space: nowrap; }

  .agree { left: 232px; display: flex; align-items: center; gap: 7px; color: var(--brand-blue); font-size: 13.5px; }
  .agree-box { width: 19px; height: 19px; border: 1px solid var(--brand-blue); background: var(--white); }

  .terms { left: 66px; top: 791px; width: 774px; font-size: 11.4px; line-height: 14px; color: var(--muted); text-align: justify; }

  .sign-line { top: 1086px; height: 1.5px; background: var(--brand-teal); }
  .sign-label { top: 1100px; font-size: 13.5px; color: var(--label); text-align: center; }

  .footer-main { left: 0; top: 1131px; width: 738px; height: 69px; background: linear-gradient(90deg, var(--brand-blue), var(--brand-blue-mid)); color: var(--white); font-weight: 700; font-size: 16px; line-height: 20px; padding: 13px 0 0 62px; }
  .footer-accent { left: 741px; top: 1131px; width: 155px; height: 69px; background: var(--brand-teal); }
</style>
</head>
<body>
  <div class="page-panel"></div>

  <div class="abs brand">
    <div class="brand-name">PINECREST</div>
    <div class="brand-sub">INSURANCE SERVICES</div>
  </div>

  <div class="abs auth-title">PAYMENT AUTHORIZATION FORM</div>
  <table class="abs auth-table">
    <tr><td class="label">INSURED'S NAME</td><td></td></tr>
    <tr><td class="label">LINE OF INSURANCE</td><td></td></tr>
    <tr><td class="label">EFFECTIVE DATES</td><td></td></tr>
  </table>

  <div class="abs band" style="top:185px;">
    <span class="band-title">ACH PAYMENT</span>
    <span class="band-option">SELECT PAYMENT OPTION <span class="option-box"></span></span>
  </div>
  <table class="abs field-table" style="top:220px;">
    <tr><td class="label">Bank Account Type</td><td><span class="hint">(Account Types: Checking, Savings, Business, Consumer</span></td></tr>
    <tr><td class="label">Name on account</td><td></td></tr>
    <tr><td class="label">Routing Number</td><td><span class="hint">(Routing number must include a total of 9 digits)</span></td></tr>
    <tr><td class="label">Account Number</td><td></td></tr>
    <tr><td class="label">Phone Number</td><td></td></tr>
  </table>
  <table class="abs pay-table" style="left:232px; top:379px; width:620px;">
    <tr>
      <td style="width:130px;">TOTAL PAYMENT</td>
      <td style="width:341px;"></td>
      <td style="width:47px;">DATE</td>
      <td></td>
    </tr>
  </table>
  <div class="abs agree" style="top:421px;"><span class="agree-box"></span>By checking this box you agree to use this account for all future transactions.</div>

  <div class="abs band" style="top:454px;">
    <span class="band-title">CREDIT CARD</span>
    <span class="band-note">(cc processing fees apply and will never exceed 3.5% of the balance due)</span>
    <span class="band-option">SELECT PAYMENT OPTION <span class="option-box"></span></span>
  </div>
  <table class="abs field-table" style="top:488px;">
    <tr><td class="label">Credit Card Number</td><td></td></tr>
    <tr><td class="label">Expiration Date</td><td></td></tr>
    <tr><td class="label">CVV</td><td></td></tr>
    <tr><td class="label">Name on Card</td><td></td></tr>
    <tr><td class="label">Street Address</td><td></td></tr>
    <tr><td class="label">Zip Code</td><td></td></tr>
  </table>
  <table class="abs pay-table" style="left:232px; top:682px; width:620px;">
    <tr>
      <td style="width:130px;">DOWN PAYMENT</td>
      <td style="width:114px;"></td>
      <td style="width:132px;">TOTAL PAYMENT</td>
      <td style="width:108px;"></td>
      <td style="width:49px;">DATE</td>
      <td></td>
    </tr>
  </table>
  <div class="abs agree" style="top:722px;"><span class="agree-box"></span>By checking this box you agree to use this account for all future transactions.</div>

  <div class="abs band" style="top:754px;">
    <span class="band-title" style="margin-left:-4px;">TERMS OF SERVICE</span>
  </div>
  <p class="abs terms">I authorize Pinecrest Insurance (PC) to use the selected payment method on file to pay my insurance premium, deposit adjustments (if applicable) and any fees or taxes that are due. This authorization is to remain in full force until Pinecrest has received notification of its termination in such time and in such manner to afford PC responsible opportunity to act upon it. If credit option is selected Pinecrest will impose a surcharge on credit cards that will not be greater than our cost of acceptance. This surcharge may fluctuate, however, it will never exceed 3.5% of the balance due. If I need to make any changes to the account information on file, I will email PC and provide updated information. This authorization applies to any subsequent accounts provided and is to remain in full force until PC has received notification of its termination in such time and in such manner to afford PC reasonable opportunity to act upon it. PLEASE NOTE: We will charge a $15.00 fee for any payment that is declined or returned. If payment is declined or returned more than once in a 3-month period, coverage may be cancelled and not eligible for reinstatement with current carrier. If policy can be reinstated additional reinstatement fees may apply.</p>

  <div class="abs sign-line" style="left:77px; width:440px;"></div>
  <div class="abs sign-line" style="left:539px; width:297px;"></div>
  <div class="abs sign-label" style="left:77px; width:440px;">SIGNATURE</div>
  <div class="abs sign-label" style="left:539px; width:297px;">DATE</div>

  <div class="abs footer-main">THANK YOU FOR CHOOSING PINECREST<br>&nbsp;QUESTIONS OR COMMENTS 555.317.2096</div>
  <div class="abs footer-accent"></div>
</body>
</html>
```